Bluestone Health Clinic needs a newspaper ad design

We need a newspaper ad for our Health Clinic. We provide primary medical care, medicated addiction therapy, psychiatric care, and psychotherapy in person and would really like to promote our teletherapy. So I have attached our company logo as well.

```html
<!DOCTYPE html>
<html lang="en">
<head>
<meta charset="utf-8">
<title>Bluestone Health Clinic – Newspaper Ad</title>
<link rel="stylesheet" href="https://fonts.googleapis.com/css2?family=Tinos:wght@400;700&display=swap">
<style>
  :root {
    --navy: #0a4a94;
    --band-blue: #034a90;
    --red: #c2000f;
    --red-deep: #a80008;
    --white: #ffffff;
    --ink: #1a1a1a;
    --sky-1: #cfe3f4;
    --sky-2: #eaf4fc;
    --stage: #e4e4e4;
  }
  html, body {
    margin: 0;
    padding: 0;
    width: 990px;
    height: 1200px;
    overflow: hidden;
    background: var(--stage);
  }
  .ad {
    position: absolute;
    left: 31px;
    top: 0;
    width: 928px;
    height: 1200px;
  }
  .ad svg { display: block; }
  .serif { font-family: "Tinos", "Times New Roman", serif; }
  .brand-name { font-size: 40px; font-weight: 400; fill: var(--ink); }
  .brand-tagline { font-size: 26px; font-weight: 400; fill: var(--ink); }
  .headline-top { font-size: 55px; font-weight: 700; fill: var(--navy); }
  .headline-mid { font-size: 84px; font-weight: 700; fill: var(--red); }
  .headline-box-text { font-size: 84px; font-weight: 700; fill: var(--white); }
  .services-title { font-size: 52px; font-weight: 700; fill: var(--white); }
  .service-item { font-size: 27px; font-weight: 700; fill: var(--white); }
  .phone-number { font-size: 63px; font-weight: 700; fill: var(--white); }
  .website { font-size: 35px; font-weight: 700; fill: var(--white); }
  .address { font-size: 20.5px; font-weight: 700; fill: var(--white); }
</style>
</head>
<body>
<main class="ad">
  <svg width="928" height="1200" viewBox="0 0 928 1200" xmlns="http://www.w3.org/2000/svg" class="serif">
    <defs>
      <linearGradient id="backdrop-tone" x1="0" y1="0" x2="1" y2="0.3">
        <stop offset="0" stop-color="var(--sky-1)"/>
        <stop offset="0.75" stop-color="var(--sky-2)"/>
        <stop offset="1" stop-color="#dbeaf6"/>
      </linearGradient>
      <radialGradient id="group-tone" cx="0.55" cy="0.55" r="0.6">
        <stop offset="0" stop-color="#f4f6f8" stop-opacity="1"/>
        <stop offset="0.45" stop-color="#d9d2cc" stop-opacity="0.95"/>
        <stop offset="0.75" stop-color="#b9cde2" stop-opacity="0.7"/>
        <stop offset="1" stop-color="#cfe3f4" stop-opacity="0"/>
      </radialGradient>
      <linearGradient id="nurse-tone" x1="0" y1="0" x2="1" y2="1">
        <stop offset="0" stop-color="#eef1f3"/>
        <stop offset="0.55" stop-color="#c9d6dc"/>
        <stop offset="1" stop-color="#4f8c9a"/>
      </linearGradient>
    </defs>

    <!-- backdrop -->
    <rect class="backdrop" x="0" y="0" width="928" height="1200" fill="url(#backdrop-tone)"/>

    <!-- hero photo area -->
    <rect class="hero-photo" x="420" y="190" width="500" height="560" rx="40" fill="url(#group-tone)"
          role="img" aria-label="Photo of a smiling doctor holding a clipboard beside a mother and her young daughter in a bright clinic"/>

    <!-- colour bands -->
    <polygon class="band-blue" points="0,551 928,702 928,1200 0,1200" fill="var(--band-blue)"/>
    <polygon class="band-red-deep" points="0,1058 928,907 928,1200 0,1200" fill="var(--red-deep)"/>
    <polygon class="band-red" points="0,1082 928,945 928,1200 0,1200" fill="var(--red)"/>

    <!-- brand -->
    <circle class="brand-mark" cx="140" cy="128" r="30" fill="var(--navy)"/>
    <text class="brand-name" x="196" y="125" textLength="630" lengthAdjust="spacingAndGlyphs">Harlow Medical &amp; Associates, LLC</text>
    <text class="brand-tagline" x="228" y="166" textLength="560" lengthAdjust="spacingAndGlyphs">Dedicated to Hope, Healing &amp; Recovery</text>

    <!-- headline -->
    <text class="headline-top" x="97" y="317" textLength="337" lengthAdjust="spacingAndGlyphs">BLUESTONE</text>
    <text class="headline-mid" x="97" y="392" textLength="337" lengthAdjust="spacingAndGlyphs">HEALTH</text>
    <rect class="headline-box" x="100" y="402" width="330" height="79" fill="var(--red)"/>
    <text class="headline-box-text" x="265" y="470" text-anchor="middle">CLINIC</text>

    <!-- services -->
    <text class="services-title" x="95" y="686">OUR</text>
    <text class="services-title" x="95" y="734">SERVICES</text>
    <rect class="services-rule" x="97" y="749" width="292" height="2.5" fill="var(--white)"/>

    <g class="service-list">
      <g class="tick" fill="none" stroke="var(--white)" stroke-width="1.6">
        <circle cx="106" cy="790" r="8.5"/><polyline points="102,790 105,793 110,787"/>
        <circle cx="106" cy="832" r="8.5"/><polyline points="102,832 105,835 110,829"/>
        <circle cx="106" cy="872" r="8.5"/><polyline points="102,872 105,875 110,869"/>
        <circle cx="106" cy="913" r="8.5"/><polyline points="102,913 105,916 110,910"/>
        <circle cx="106" cy="955" r="8.5"/><polyline points="102,955 105,958 110,952"/>
      </g>
      <text class="service-item" x="125" y="799">Primary Medical Care</text>
      <text class="service-item" x="125" y="841">Medicated Addiction Therapy</text>
      <text class="service-item" x="125" y="881">Psychiatric Care</text>
      <text class="service-item" x="125" y="922">Psychotherapy In Person</text>
      <text class="service-item" x="125" y="964">Teletherapy</text>
    </g>

    <!-- hexagon photo frame -->
    <polygon class="hex-photo" points="680,616 858,714 858,906 680,1004 500,906 500,714"
             fill="url(#nurse-tone)" stroke="var(--white)" stroke-width="8" stroke-linejoin="round"
             role="img" aria-label="Photo of a smiling nurse in teal scrubs seated at a laptop"/>

    <!-- contact -->
    <g class="phone-icon">
      <circle cx="476" cy="1073" r="24" fill="var(--white)"/>
      <circle cx="476" cy="1073" r="19" fill="var(--navy)"/>
      <path d="M470 1062 c-4 2 -5 6 -3 11 c2 6 6 10 11 12 c4 1 7 0 9 -3 l-4 -4 c-1 -1 -2 -1 -3 0 l-2 2 c-3 -1 -6 -4 -7 -7 l2 -2 c1 -1 1 -2 0 -3 z" fill="var(--white)"/>
    </g>
    <text class="phone-number" x="516" y="1095">0123 456 789</text>

    <g class="globe-icon" fill="none" stroke="var(--white)" stroke-width="1.8">
      <circle cx="463" cy="1130" r="11"/>
      <ellipse cx="463" cy="1130" rx="5" ry="11"/>
      <line x1="452" y1="1130" x2="474" y2="1130"/>
      <path d="M454 1124 h18 M454 1136 h18"/>
    </g>
    <text class="website" x="488" y="1142">www.harlowmedical.com</text>

    <g class="pin-icon" fill="none" stroke="var(--white)" stroke-width="1.6">
      <circle cx="102" cy="1102" r="4.5"/>
      <line x1="102" y1="1107" x2="102" y2="1116"/>
      <line x1="97" y1="1117" x2="107" y2="1117"/>
    </g>
    <text class="address" x="120" y="1118">Address Line 1,</text>
    <text class="address" x="120" y="1142">Address Line 2, Address Line 2</text>
  </svg>
</main>
</body>
</html>
```